Flyer-Design für Zweithaar Studio
Zielgruppe
Firma MOLVA Ketz ist ein Zweithaar Studio. Hier erhalten Kunden individuell auf sie zugeschnittene Perücken und Toupets. Unsere Zielgruppe sind Männer und Frauen mit wenig oder keiner Kopfbehaarung oder Menschen die krankheitsbedingt unter Haarausfall leiden.
Aufgabenstellung
Bitte Vorschläge zu Anzahl Seiten und Format erstellen, aktuell haben wir noch keine Vorstellung dazu. Folgende Inhalte haben wir schon mal als Entwurf vorbereitet:
Eine Seite zum Thema Toupets mit dem Bild vom Mann:
Leiden Sie an übermäßigem Haarausfall?
Fühlen Sie sich nicht mehr 100% wohl damit und möchten gerne wieder Ihre Attraktivität und vor allem das Wohlbefinden steigern?
Dann sind Sie bei uns sehr gut aufgehoben, denn wir können Ihnen Ihr Toupet individuell auf Ihre Bedürfnisse hin z.B. Farbe, Grauanteil, Größe und Styling anpassen.
Eine Seite zum Thema Perücken mit dem Bild der Frau:
Sind Sie an einer Perücke interessiert die augenscheinlich keinen Unterschied zu gewachsenem Haar aufweist?
Dann sind Sie bei uns an der richtigen Adresse. Die langjährige Erfahrung im Zweithaar Bereich von Friseurmeisterin verspricht Ihnen optimale Beratung und ein individuell auf Sie abgestimmtes Produkt.
Bei uns erhalten Sie Zugriff auf verschiedene Modelle im gesamten Preisspektrum.
Liegt eine von Ihrem Arzt attestierte Erkrankung vor, übernimmt Ihre Krankenkasse höchstwahrscheinlich die Kosten für Ihr Zweithaar. Die Formalitäten dazu erledigen wir gerne für Sie um Ihnen unnötigen Stress zu ersparen.
Eine weitere Seite mit den besonderen Merkmalen mit dem Bild Diversity:
Mit unserer Befestigungsmethode sind Sie sehr flexibel - starker halt für jede Situation und auf Wunsch auch abnehmbar z.B. nachts beim schlafen.
Der große Vorteil unserer Befestigungsmethode liegt darin, dass Sie diese selbst umsetzen können und somit nicht jeden Monat das Studio zur Neubefestigung aufsuchen müssen. Das spart Ihnen Zeit und Geld.
Wir können Ihnen Toupets und Perücken in allen Preisklassen anbieten, in verschiedenen Farben, auf Wunsch mit Grauanteil passend zum Alter des Trägers. Unsere Friseurmeisterin Frau Tiltrop berät Sie gerne, natürlich unverbindlich und kostenlos.

```html
<!DOCTYPE html>
<html lang="de">
<head>
<meta charset="utf-8">
<title>MOLVA Ketz – Flyer Zweithaar Studio</title>
<link rel="stylesheet" href="https://fonts.googleapis.com/css2?family=Playfair+Display:wght@700&family=Inter:wght@300;400&display=swap">
<style>
  :root {
    --stage: #a3a5a4;
    --ink: #1c1b1a;
    --ink-deep: #0d0b0b;
    --maroon: #3a1518;
    --cream: #ece9e4;
    --text-dark: #222;
    --text-light: #e9e5e0;
    --rule: #8a8580;
    --panel-w: 260px;
    --panel-h: 600px;
  }
  * { box-sizing: border-box; margin: 0; padding: 0; }
  html, body { width: 1200px; height: 3142px; overflow: hidden; }
  body {
    background: var(--stage);
    position: relative;
    font-family: "Inter", Arial, sans-serif;
    font-weight: 300;
    color: var(--text-light);
  }
  .spread {
    position: absolute;
    height: var(--panel-h);
    display: flex;
    box-shadow: 0 18px 40px rgba(0,0,0,.25);
  }
  .spread--outside { left: 340px; top: 200px; width: 520px; }
  .spread--toupet  { left: 340px; top: 1150px; width: 520px; }
  .spread--inside  { left: 80px;  top: 2150px; width: 1040px; }

  .panel {
    position: relative;
    width: var(--panel-w);
    height: var(--panel-h);
    overflow: hidden;
    background: var(--ink);
  }
  .panel + .panel { border-left: 1px solid rgba(255,255,255,.06); }

  .photo { position: absolute; left: 0; top: 0; }

  .headline {
    font-family: "Playfair Display", Georgia, serif;
    font-weight: 700;
    text-transform: uppercase;
    letter-spacing: .06em;
    line-height: 1;
  }
  .subline { font-weight: 300; letter-spacing: .02em; }

  /* Outside */
  .contact-area {
    position: absolute; left: 0; top: 0; width: 100%; height: 330px;
    background: var(--cream); color: var(--text-dark);
    padding: 110px 30px 0; text-align: right;
  }
  .contact-title { font-size: 26px; font-weight: 400; margin-bottom: 14px; }
  .contact-line { font-size: 11px; line-height: 18px; }
  .brand-area {
    position: absolute; left: 0; bottom: 0; width: 100%; height: 270px;
    display: flex; align-items: center; justify-content: center;
  }
  .brand-name {
    font-family: "Playfair Display", Georgia, serif;
    font-weight: 700; font-size: 30px; letter-spacing: .08em;
    color: var(--text-light); text-transform: uppercase;
    padding: 8px 0; border-top: 1px solid var(--rule); border-bottom: 1px solid var(--rule);
  }
  .cover-photo { width: 260px; height: 330px; }
  .cover-claim {
    position: absolute; left: 0; bottom: 0; width: 100%; height: 270px;
    text-align: center; padding-top: 48px;
  }
  .cover-claim .subline { font-size: 24px; }
  .cover-claim .headline { font-size: 34px; margin: 6px 0; }

  /* Toupet */
  .toupet-photo { width: 520px; height: 320px; }
  .toupet-title { position: absolute; left: 24px; top: 392px; }
  .toupet-title .headline { font-size: 30px; }
  .toupet-title .subline { font-size: 22px; margin-top: 4px; }
  .body-copy { font-size: 11px; line-height: 16px; }
  .body-copy p + p { margin-top: 8px; }
  .toupet-copy { position: absolute; left: 22px; right: 22px; top: 350px; }

  /* Inside */
  .inside-dark { position: absolute; left: 0; top: 0; width: 520px; height: 430px; background: var(--ink-deep); }
  .diversity-photo { top: 430px; width: 520px; height: 170px; }
  .why-title { position: absolute; left: 26px; top: 180px; }
  .why-title .headline { font-size: 28px; }
  .why-title .subline { font-size: 20px; margin-top: 4px; }
  .why-copy { position: absolute; left: 282px; top: 36px; width: 218px; font-size: 10px; line-height: 14.5px; }
  .wig-photo { left: 520px; width: 520px; height: 370px; }
  .wig-band { position: absolute; left: 520px; top: 370px; width: 520px; height: 230px; background: var(--maroon); }
  .wig-title { position: absolute; left: 544px; top: 290px; }
  .wig-title .headline { font-size: 28px; }
  .wig-title .subline { font-size: 20px; margin-top: 4px; }
  .wig-copy-a { position: absolute; left: 544px; top: 396px; width: 214px; font-size: 10px; line-height: 14.5px; }
  .wig-copy-b { position: absolute; left: 804px; top: 300px; width: 214px; font-size: 10px; line-height: 14.5px; }
  .fold { position: absolute; top: 0; width: 1px; height: 100%; background: rgba(255,255,255,.07); }
</style>
</head>
<body>

  <!-- Outside: contact panel + cover -->
  <section class="spread spread--outside">
    <div class="panel panel--contact">
      <div class="contact-area">
        <h2 class="contact-title">Kontakt</h2>
        <p class="contact-line">Inhaber Nachname</p>
        <p class="contact-line">Adresszeile 1</p>
        <p class="contact-line">1234 Adresse</p>
        <p class="contact-line">Tel.: 0123 456 78</p>
        <p class="contact-line">info@webadresse.de</p>
        <p class="contact-line">www.webadresse.de</p>
      </div>
      <div class="brand-area">
        <span class="brand-name">MOLVA Ketz</span>
      </div>
    </div>
    <div class="panel panel--cover">
      <svg class="photo cover-photo" role="img" aria-label="Foto: Frau mit dunklem, zerzaustem Haar blickt besorgt auf ausgefallene Haare" viewBox="0 0 260 330" preserveAspectRatio="none">
        <defs>
          <linearGradient id="coverTone" x1="0" y1="0" x2="0" y2="1">
            <stop offset="0" stop-color="#c9cde6"/>
            <stop offset=".55" stop-color="#8c7b7c"/>
            <stop offset="1" stop-color="#6a1a22"/>
          </linearGradient>
        </defs>
        <rect width="260" height="330" fill="url(#coverTone)"/>
      </svg>
      <div class="cover-claim">
        <p class="subline">Haben Sie</p>
        <p class="headline">Genug<br>Haare</p>
        <p class="subline">gelassen?</p>
      </div>
    </div>
  </section>

  <!-- Toupet spread -->
  <section class="spread spread--toupet">
    <div class="panel"></div>
    <div class="panel"></div>
    <svg class="photo toupet-photo" role="img" aria-label="Foto: Mann in dunkler Jacke sitzt lächelnd vor dunkler Holzwand" viewBox="0 0 520 320" preserveAspectRatio="none">
      <defs>
        <linearGradient id="toupetTone" x1="0" y1="0" x2="1" y2="0">
          <stop offset="0" stop-color="#17161c"/>
          <stop offset=".45" stop-color="#2b3145"/>
          <stop offset="1" stop-color="#0b0a0c"/>
        </linearGradient>
      </defs>
      <rect width="520" height="320" fill="url(#toupetTone)"/>
    </svg>
    <div class="fold" style="left:260px"></div>
    <div class="toupet-title">
      <p class="headline">Toupets</p>
      <p class="subline">zum Wohlfühlen</p>
    </div>
    <div class="toupet-copy body-copy" style="left:282px; width:218px;">
      <p>Leiden Sie an übermäßigem Haarausfall? Fühlen Sie sich nicht mehr 100% wohl damit und möchten gerne wieder Ihre Attraktivität und vor allem das Wohlbefinden steigern?</p>
      <p>Dann sind Sie bei uns sehr gut aufgehoben, denn wir können Ihnen Ihr Toupet individuell auf Ihre Bedürfnisse hin z.B. Farbe, Grauanteil, Größe und Styling anpassen.</p>
    </div>
  </section>

  <!-- Inside spread -->
  <section class="spread spread--inside">
    <div class="panel"></div><div class="panel"></div><div class="panel"></div><div class="panel"></div>
    <div class="inside-dark"></div>
    <svg class="photo diversity-photo" role="img" aria-label="Fotoreihe: lächelnde Porträts verschiedener Menschen" viewBox="0 0 520 170" preserveAspectRatio="none">
      <defs>
        <linearGradient id="diversityTone" x1="0" y1="0" x2="1" y2="0">
          <stop offset="0" stop-color="#5a4638"/>
          <stop offset=".5" stop-color="#8a7868"/>
          <stop offset="1" stop-color="#4c4744"/>
        </linearGradient>
      </defs>
      <rect width="520" height="170" fill="url(#diversityTone)"/>
    </svg>
    <svg class="photo wig-photo" role="img" aria-label="Foto: Frau mit langem, rotbraunem Haar vor schwarzem Hintergrund" viewBox="0 0 520 370" preserveAspectRatio="none">
      <defs>
        <radialGradient id="wigTone" cx=".5" cy=".35" r=".6">
          <stop offset="0" stop-color="#5a2a24"/>
          <stop offset=".5" stop-color="#241312"/>
          <stop offset="1" stop-color="#0b0909"/>
        </radialGradient>
      </defs>
      <rect width="520" height="370" fill="url(#wigTone)"/>
    </svg>
    <div class="wig-band"></div>
    <div class="fold" style="left:260px"></div>
    <div class="fold" style="left:520px"></div>
    <div class="fold" style="left:780px"></div>

    <div class="why-title">
      <p class="headline">Warum</p>
      <p class="subline">bei uns kaufen?</p>
    </div>
    <div class="why-copy body-copy">
      <p>Mit unserer Befestigungsmethode sind Sie sehr flexibel – starker Halt für jede Situation und auf Wunsch auch abnehmbar z.B. nachts beim Schlafen.</p>
      <p>Der große Vorteil unserer Befestigungsmethode liegt darin, dass Sie diese selbst umsetzen können und somit nicht jeden Monat das Studio zur Neubefestigung aufsuchen müssen. Das spart Ihnen Zeit und Geld.</p>
      <p>Wir können Ihnen Toupets und Perücken in allen Preisklassen anbieten, in verschiedenen Farben, auf Wunsch mit Grauanteil passend zum Alter des Trägers. Unsere Friseurmeisterin Frau Tiltrop berät Sie gerne, natürlich unverbindlich und kostenlos.</p>
    </div>

    <div class="wig-title">
      <p class="headline">Perücken</p>
      <p class="subline">für Natürlichkeit</p>
    </div>
    <div class="wig-copy-a body-copy">
      <p>Sind Sie an einer Perücke interessiert die augenscheinlich keinen Unterschied zu gewachsenem Haar aufweist? Dann sind Sie bei uns an der richtigen Adresse.</p>
      <p>Die langjährige Erfahrung im Zweithaar Bereich von Friseurmeisterin Frau Tiltrop verspricht Ihnen optimale Beratung und ein individuell auf Sie abgestimmtes Produkt.</p>
    </div>
    <div class="wig-copy-b body-copy" style="top:396px">
      <p>Bei uns erhalten Sie Zugriff auf verschiedene Modelle im gesamten Preisspektrum.</p>
      <p>Liegt eine von Ihrem Arzt attestierte Erkrankung vor, übernimmt Ihre Krankenkasse höchstwahrscheinlich die Kosten für Ihr Zweithaar. Die Formalitäten dazu erledigen wir gerne für Sie um Ihnen unnötigen Stress zu ersparen.</p>
    </div>
  </section>

</body>
</html>
```